Website re-design

We are a successful furnished apartment provider in Boston. We currently are working on re-designing our website www.ribtenlofts.com to make it more modern, designer look and user friendly. We hired a designer, but are not happy with the designs proposed and want to improve on them. The winning design will be paid regardless of whether we stay with our current designer or not. We want ideas and functional page links to see how it will work. Platform we have chosen is wordpress. Feel free to propose others easy for us to update and modify. We do not like Joomla on which website is currently running. We do not like flash nor long load times.
Please use photos on our website for design presentations. www.ribtenlofts.com

Target Market(s)

doctors, nurses, business men but mostly business women, some post-medical students

Industry/Entity Type

Apartment

Requirements
Must have
• Quick action button for reservation form and a notification and email forwarding system to us of reservation information by potential clients. Blog required with feedback by guests allowed, we can censor which are published. Slide shows of apartments.
Should not have
• No movies.

```html
<!DOCTYPE html>
<html lang="en">
<head>
<meta charset="utf-8">
<title>Ribten Lofts – Furnished Apartments</title>
<link href="https://fonts.googleapis.com/css2?family=Marcellus&family=PT+Sans:wght@400;700&display=swap" rel="stylesheet">
<style>
  :root {
    --page-bg: #e4e4e4;
    --header-bg: #ececec;
    --content-bg: #f6f6f6;
    --footer-bg: #eaeaea;
    --panel: #302e2c;
    --panel-line: #6b6763;
    --nav-btn: #4a4a4a;
    --nav-text: #ffffff;
    --gold: #c9b06a;
    --brand-text: #3a2f25;
    --accent-yellow: #f2da8c;
    --phone-orange: #f0a820;
    --pill: #f7e6d6;
    --pill-arrow: #b0432c;
    --action-blue: #176a8d;
    --field: #9a9a9a;
    --label: #e6e0d6;
    --ink: #1f1f1f;
    --link-blue: #1e6a9a;
    --muted: #7a7a7a;
    --social-a: #3ba3d6;
    --social-b: #d8d8d8;
  }
  * { box-sizing: border-box; margin: 0; padding: 0; }
  html, body { width: 1200px; height: 900px; overflow: hidden; }
  body {
    position: relative;
    background: var(--page-bg);
    font-family: "PT Sans", Arial, sans-serif;
    color: var(--ink);
  }
  .site-header {
    position: absolute; left: 0; top: 0; width: 1200px; height: 123px;
    background: repeating-linear-gradient(135deg, var(--header-bg) 0 3px, #e6e6e6 3px 6px);
  }
  .brand { position: absolute; left: 37px; top: 29px; display: flex; align-items: center; }
  .brand-dot { width: 72px; height: 72px; border-radius: 50%; background: var(--gold); }
  .brand-text { margin-left: 20px; }
  .brand-name {
    font-family: "Marcellus", Georgia, serif; font-size: 42px; line-height: 1;
    color: var(--brand-text); letter-spacing: 0.5px;
  }
  .brand-tagline {
    font-size: 14px; letter-spacing: 3.6px; color: var(--brand-text); margin-top: 6px;
  }
  .phone { position: absolute; left: 955px; top: 14px; display: flex; align-items: center; }
  .phone-icon { width: 33px; height: 33px; border-radius: 4px; background: var(--action-blue); display: flex; align-items: center; justify-content: center; }
  .phone-number { margin-left: 10px; color: var(--phone-orange); font-size: 19px; margin-top: 8px; }
  .main-nav { position: absolute; top: 71px; left: 0; }
  .main-nav a {
    position: absolute; height: 30px; background: var(--nav-btn); color: var(--nav-text);
    border-radius: 4px; font-size: 16px; text-decoration: none;
    display: flex; align-items: center; justify-content: center;
    box-shadow: 0 1px 2px rgba(0,0,0,.3);
  }
  .content {
    position: absolute; left: 319px; top: 123px; width: 881px; height: 692px;
    background: var(--content-bg);
  }
  .hero {
    position: absolute; left: 405px; top: 150px; width: 666px; height: 386px;
    border: 5px solid #fff; box-shadow: 0 0 3px rgba(0,0,0,.2);
    background: linear-gradient(100deg, #4d5a3a 0%, #7a4a3a 35%, #8a5a48 55%, #5b6a48 75%, #3f4a34 100%);
  }
  .welcome-title {
    position: absolute; left: 404px; top: 560px; width: 452px; padding-bottom: 3px;
    font-size: 17px; font-weight: 400; border-bottom: 1px dashed #8a8a8a;
  }
  .intro {
    position: absolute; left: 404px; top: 611px; width: 694px;
    font-size: 14.5px; line-height: 17px;
  }
  .like-line {
    position: absolute; left: 404px; top: 738px; display: flex; align-items: center;
    color: var(--link-blue); font-size: 15px;
  }
  .like-square { width: 36px; height: 35px; background: #3b5998; margin-left: 8px; }
  .site-footer {
    position: absolute; left: 0; top: 815px; width: 1200px; height: 85px;
    background: repeating-linear-gradient(135deg, var(--footer-bg) 0 3px, #e3e3e3 3px 6px);
    border-top: 1px solid #d6d6d6;
  }
  .copyright { position: absolute; left: 0; width: 1408px; text-align: center; top: 28px; font-size: 14px; color: var(--muted); }
  .follow { position: absolute; left: 1083px; top: 10px; }
  .follow-label { color: #f5e000; font-size: 13px; }
  .follow-icons { display: flex; margin-top: 2px; }
  .follow-icons span { width: 38px; height: 34px; }
  .follow-icons .one { background: var(--social-a); }
  .follow-icons .two { background: var(--social-b); }
  .panel { position: absolute; background: var(--panel); border-radius: 4px; }
  .reservation { left: 28px; top: 184px; width: 273px; height: 288px; }
  .panel-title {
    position: absolute; left: 30px; width: 213px; text-align: center; padding-bottom: 2px;
    border-bottom: 1px dashed var(--panel-line);
  }
  .reservation .panel-title { top: 22px; color: var(--accent-yellow); font-size: 21px; }
  .field-label { position: absolute; color: var(--label); font-size: 14px; }
  .pill {
    position: absolute; height: 29px; background: var(--pill); border-radius: 7px;
    font-size: 13px; color: #8a7a6a; display: flex; align-items: center; padding-left: 12px;
  }
  .pill::after {
    content: ""; position: absolute; right: 7px; top: 13px;
    border-left: 4px solid transparent; border-right: 4px solid transparent; border-top: 5px solid var(--pill-arrow);
  }
  .pill::before { content: ""; position: absolute; right: 19px; top: 6px; height: 17px; border-left: 1px solid #d9bca8; }
  .search-btn {
    position: absolute; left: 132px; top: 233px; width: 113px; height: 32px;
    background: var(--action-blue); border: 2px solid #fff; color: #fff; font-size: 17px;
    display: flex; align-items: center; justify-content: center;
  }
  .email { left: 30px; top: 482px; width: 271px; height: 316px; }
  .email .panel-title { top: 10px; left: 40px; width: 244px; color: #fff; font-size: 18px; text-align: left; padding-left: 30px; height: 28px; }
  .at-icon { position: absolute; left: 138px; top: 6px; }
  .input { position: absolute; background: var(--field); }
  .send-btn {
    position: absolute; left: 163px; top: 296px; width: 89px; height: 24px;
    background: var(--action-blue); border: 1px solid #fff; color: #fff; font-size: 14px; font-weight: 700;
    display: flex; align-items: center; justify-content: center;
  }
</style>
</head>
<body>
  <header class="site-header">
    <div class="brand">
      <div class="brand-dot"></div>
      <div class="brand-text">
        <div class="brand-name">RIBTEN LOFTS</div>
        <div class="brand-tagline">FURNISHED APARTMENTS</div>
      </div>
    </div>
    <div class="phone">
      <div class="phone-icon">
        <svg width="20" height="22" viewBox="0 0 20 22" aria-hidden="true">
          <path d="M4 2 L8 2 L9 7 L6.5 8.5 C7.5 11.5 9.5 14 12.5 15.5 L14 13 L19 14 L19 18 C19 19.5 18 20.5 16.5 20.5 C8.5 20 2 13.5 1.5 5 C1.5 3.5 2.5 2 4 2 Z" fill="#fff"/>
        </svg>
      </div>
      <span class="phone-number">617 555 0142</span>
    </div>
    <nav class="main-nav">
      <a href="#" style="left:420px;width:77px">Home</a>
      <a href="#" style="left:517px;width:116px">Apartments</a>
      <a href="#" style="left:645px;width:84px">Blog</a>
      <a href="#" style="left:738px;width:88px">Reviews</a>
      <a href="#" style="left:836px;width:87px">Contact</a>
      <a href="#" style="left:935px;width:85px">Boston</a>
      <a href="#" style="left:1035px;width:88px">About Us</a>
    </nav>
  </header>

  <main class="content"></main>

  <div class="hero" role="img" aria-label="Photo of a tree-lined South End street with red brick row houses, black iron railings and a brick sidewalk"></div>

  <h1 class="welcome-title">Welcome to Ribten Lofts Furnished Apartments</h1>
  <p class="intro">Ribten Lofts is proud to offer some of the best furnished apartments in Boston. Our locations are in the trendiest area of the city: the South End. In the South End neighborhood, you will find wonderful restaurants, theaters, cafes and artist lofts. Our short term and extended stay apartments are very, very clean. We also offer the latest designer layouts: hardwood floors, Wireless Dsl, Cable TV, flat screen in most apartments, washer and dryer, cookware, cotton linens. Please click links on left for photo galleries, pricing, availability and reservation form and write us for more information. Thank you.</p>
  <div class="like-line">If you are on Friendspace, please "like" us! <span class="like-square"></span></div>

  <section class="panel reservation">
    <h2 class="panel-title">Quick Reservation</h2>
    <span class="field-label" style="left:25px;top:62px">Chick In Date :</span>
    <div class="pill" style="left:25px;top:91px;width:94px">Tue 21</div>
    <div class="pill" style="left:128px;top:91px;width:124px">DECEMBER</div>
    <span class="field-label" style="left:28px;top:140px">Chick Out Date :</span>
    <div class="pill" style="left:25px;top:173px;width:94px">Tue 21</div>
    <div class="pill" style="left:128px;top:173px;width:124px">DECEMBER</div>
    <div class="search-btn">Search</div>
  </section>

  <section class="panel email">
    <h2 class="panel-title">E-mail</h2>
    <svg class="at-icon" width="40" height="40" viewBox="0 0 40 40" aria-hidden="true">
      <circle cx="20" cy="20" r="18" fill="#d8d8d8"/>
      <circle cx="20" cy="20" r="13" fill="none" stroke="#555" stroke-width="3"/>
      <circle cx="20" cy="20" r="5" fill="none" stroke="#555" stroke-width="3"/>
      <path d="M25 14 L25 23 C25 27 31 27 32 22" fill="none" stroke="#555" stroke-width="3"/>
    </svg>
    <span class="field-label" style="left:24px;top:52px;font-size:13px">Enter your Name</span>
    <div class="input" style="left:24px;top:71px;width:192px;height:25px"></div>
    <span class="field-label" style="left:24px;top:102px;font-size:13px">E-mail address</span>
    <div class="input" style="left:24px;top:120px;width:192px;height:25px"></div>
    <span class="field-label" style="left:24px;top:152px;font-size:13px">Enter your Message</span>
    <div class="input" style="left:25px;top:171px;width:237px;height:119px"></div>
    <div class="send-btn">Send</div>
  </section>

  <footer class="site-footer">
    <p class="copyright">© Ribten Lofts 2010 - All Rights Reserved</p>
    <div class="follow">
      <div class="follow-label">Follow Us</div>
      <div class="follow-icons"><span class="one"></span><span class="two"></span></div>
    </div>
  </footer>
</body>
</html>
```